Label Design Brief - Quillmere Health
Label Panel Dimensions 1.25" W x 2.375" H (front/back panel)
Hello - our company develops novel products for the skin, & hair care industry as well as dietary supplements. We're looking for a label design for a new product. The product is a premium Topical hair loss/growth serum. I attached the brand logo & 2 other sister products along with some competitive products.
The product is a topical natural hair loss serum for men & women to regrow new hair and help restore hair loss & thinning hair due to vitamin deficiencies, hormone imbalance & aging. It is a science based efficacious serum with a century’s old medicinal herbal formula.
Attached is our logo & some files of other competition. The label must have an upscale, technology flair to it. The product is clinically effective, leveraged by Ancient Wisdom and Modern Science.
Below are attached files of 2 of our products & other generic competition for your perusal.

https://www.shopvarnel.example/item/K7T2QPL4XR?src=listing_offer

https://www.shopvarnel.example/item/K7T5MDR9WA/src=alt-list-view?vw=1&src=listing_lowcost

Target Market(s)

men & women age 18-80

Requirements
Must have
• see brief
Should not have
• Please do not have a picture of a man or a women on the label.

```html
<!DOCTYPE html>
<html lang="en">
<head>
<meta charset="utf-8">
<title>Quillmere Health – Growth Activator Label</title>
<link href="https://fonts.googleapis.com/css2?family=Open+Sans:wght@400;700;800&display=swap" rel="stylesheet">
<style>
  :root {
    --canvas-bg: #f6f6f6;
    --label-bg: #ebebeb;
    --ink-dark: #3b3b3b;
    --ink-body: #4a4a4a;
    --brand-brown: #6e4a3a;
    --band-start: #7b5c50;
    --band-end: #8d6b58;
    --tan: #c9976a;
    --bar-a: #7c5f56;
    --bar-b: #b8895a;
    --bar-c: #74421f;
    --icon-a: #6b3a1c;
    --icon-b: #b57a48;
  }
  * { box-sizing: border-box; margin: 0; padding: 0; }
  html, body {
    width: 1200px; height: 1200px; overflow: hidden;
    background: var(--canvas-bg);
    font-family: "Open Sans", sans-serif;
  }
  .label {
    position: absolute; left: 339px; top: 60px;
    width: 522px; height: 1080px;
    background: var(--label-bg);
  }
  .brand {
    position: absolute; top: 150px; left: 0; width: 100%;
    display: flex; align-items: center; justify-content: center; gap: 14px;
  }
  .brand-dot {
    width: 22px; height: 22px; border-radius: 50%;
    background: var(--brand-brown);
  }
  .brand-name {
    font-size: 38px; font-weight: 400; letter-spacing: 1px;
    color: var(--brand-brown);
  }
  .title {
    position: absolute; top: 355px; left: 0; width: 100%;
    text-align: center; color: var(--ink-dark);
    font-weight: 800; line-height: 1;
  }
  .title-growth { display: block; font-size: 103px; letter-spacing: -1px; }
  .title-activator { display: block; font-size: 76px; margin-top: 10px; letter-spacing: -0.5px; }
  .dht-band {
    position: absolute; top: 575px; left: 50px;
    width: 422px; height: 69px;
    background: linear-gradient(90deg, var(--band-start), var(--band-end));
    color: #f4f0ec; font-weight: 700; font-size: 58px;
    display: flex; align-items: center; justify-content: center;
    letter-spacing: -0.5px;
  }
  .audience {
    position: absolute; top: 672px; left: 0; width: 100%;
    text-align: center; color: var(--tan);
    font-size: 34px; font-weight: 400; letter-spacing: 1px;
  }
  .features {
    position: absolute; top: 853px; left: 66px;
    list-style: none; color: var(--ink-body);
    font-size: 35px; line-height: 48px;
  }
  .features li::before { content: "•"; margin-right: 6px; }
  .herb-icon {
    position: absolute; top: 815px; left: 366px;
    width: 120px; height: 165px; border-radius: 12px;
    background: linear-gradient(160deg, var(--icon-b), var(--icon-a));
    opacity: 0.85;
  }
  .volume-bar {
    position: absolute; top: 1002px; left: 60px;
    width: 294px; height: 20px;
    background: linear-gradient(90deg, var(--bar-a), var(--bar-b) 45%, var(--bar-c));
  }
  .volume {
    position: absolute; top: 990px; left: 378px;
    font-size: 34px; color: var(--ink-body);
  }
</style>
</head>
<body>
  <main class="label">
    <div class="brand">
      <span class="brand-dot"></span>
      <span class="brand-name">Quillmere Health</span>
    </div>
    <h1 class="title">
      <span class="title-growth">GROWTH</span>
      <span class="title-activator">ACTIVATOR</span>
    </h1>
    <div class="dht-band">DHT BLOCKER</div>
    <p class="audience">FOR MAN AND WOMAN</p>
    <ul class="features">
      <li>Paraben free</li>
      <li>Time - Releasel</li>
    </ul>
    <div class="herb-icon" role="img" aria-label="Icon of a mortar and pestle with herb leaves"></div>
    <div class="volume-bar"></div>
    <span class="volume">2 fl.oz</span>
  </main>
</body>
</html>
```